One page design needed for a veteran owned brewery

I need a one page web designed for a brewery that is veteran owned. We give back a portion of our proceeds to veteran based nonprofit groups. halvardbrewing.example It is word press based.

Industry/Entity Type

Craft Brewery

Number of Pages Required

1 page

```html
<!DOCTYPE html>
<html lang="en">
<head>
<meta charset="utf-8">
<title>Halvard Brewery</title>
<link href="https://fonts.googleapis.com/css2?family=Montserrat:wght@400;600;700&family=Crimson+Text:ital@1&family=Playfair+Display:ital,wght@1,700&family=Oswald:wght@400;500&display=swap" rel="stylesheet">
<style>
:root{
  --ink:#1b1c22;
  --white:#ffffff;
  --amber:#d99a4e;
  --orange:#e8950e;
  --navy:#151b27;
  --maroon:#2b0000;
  --olive:#574006;
  --grey-text:#8a8a8a;
  --card:#f7f7f7;
}
*{box-sizing:border-box;margin:0;padding:0}
html,body{width:1200px;height:2894px;overflow:hidden}
body{position:relative;font-family:"Montserrat",sans-serif;color:var(--ink);background:var(--white)}
.abs{position:absolute}
.lorem{font-family:"Crimson Text",serif;font-style:italic;font-size:14px;color:var(--grey-text);text-align:center}
.heading{font-weight:700;letter-spacing:1px;text-align:center}

/* hero */
.hero{left:0;top:0;width:1200px;height:662px;background:radial-gradient(ellipse at 40% 45%,#b97a3c 0%,#6e3b17 45%,#2f170a 100%)}
.hero-nav-brand{left:38px;top:36px;display:flex;align-items:center;gap:8px;color:var(--white);font-weight:700;font-size:15px}
.dot{display:inline-block;border-radius:50%}
.hero-nav{top:44px;left:0;width:1200px;font-size:12px;font-weight:600;color:var(--white)}
.hero-nav span{position:absolute}
.hero-title{right:155px;top:80px;text-align:right;font-weight:700;font-size:76px;line-height:76px;color:rgba(230,200,170,.55);letter-spacing:2px}
.hero-mark{left:878px;top:300px;width:250px;display:flex;align-items:center;justify-content:center;gap:12px;font-weight:700;font-size:34px;color:var(--ink)}
.slide-num{left:52px;font-size:11px;color:var(--white);font-weight:600}
.book{left:1000px;top:571px;width:138px;height:29px;border:1px solid rgba(255,255,255,.5);color:var(--amber);font-size:10px;font-weight:600;display:flex;align-items:center;justify-content:center;letter-spacing:1px}

/* perfection */
.perfection{left:0;top:662px;width:1200px;height:748px;background:radial-gradient(circle at 50% 50%,#e4e4e4 0%,#bdbdbd 60%,#a6a6a6 100%)}
.side-card{top:932px;width:390px;height:289px;background:linear-gradient(180deg,#1a2230,#121821)}
.side-card h3{position:absolute;top:104px;width:100%;text-align:center;font-size:27px;color:var(--amber);font-weight:700;letter-spacing:2px}
.side-card .rule{position:absolute;top:146px;left:175px;width:40px;height:1px;background:var(--amber)}
.side-card .lorem{position:absolute;top:160px;width:100%;color:var(--white)}
.center-card{left:430px;top:868px;width:340px;height:417px;background:var(--white)}
.center-mark{left:0;top:40px;width:340px;display:flex;flex-direction:column;align-items:center;gap:16px;font-weight:700;font-size:34px;color:var(--ink)}

/* details */
.details-bg{left:0;top:1410px;width:1200px;height:427px;background:linear-gradient(180deg,#d8a510 0%,#c67e12 60%,#a8570a 100%)}
.details-box{left:368px;top:1495px;width:463px;height:257px;background:#000}
.details-inner{left:476px;top:1572px;width:355px;height:180px;background:var(--maroon)}

/* how */
.how-bg{left:0;top:1837px;width:1200px;height:678px;background:linear-gradient(180deg,#8a560a 0%,#c2860e 45%,#eeb40c 100%)}
.feature{top:2074px;width:382px;height:177px;background:var(--card)}
.feature.dark{background:var(--navy)}
.feature h4{position:absolute;top:62px;width:100%;text-align:center;font-size:14px;font-weight:700;color:var(--amber)}
.feature .lorem{position:absolute;top:92px;width:100%}
.feature.dark .lorem{color:var(--white)}
.footer-line{left:0;top:2361px;width:1200px;height:1px;background:rgba(255,255,255,.6)}
.social{top:2464px;width:34px;height:34px;border-radius:50%;background:#b17a0c;border:1px solid #7a5206}

/* newsletter */
.news{left:0;top:2515px;width:1200px;height:379px;background:var(--olive)}
.mug{left:646px;top:2527px;width:434px;height:367px;border-radius:40px 40px 0 0;background:linear-gradient(180deg,#d9cfa0 0%,#b98a2a 25%,#8a6414 100%);opacity:.75}
.news-title{left:0;top:2585px;width:1200px;text-align:center;font-family:"Playfair Display",serif;font-style:italic;font-weight:700;font-size:45px;line-height:60px;color:var(--white)}
.email{left:382px;top:2681px;width:417px;height:37px;border:1px solid var(--white);color:var(--white);font-family:"Oswald",sans-serif;font-size:14px;display:flex;align-items:center;justify-content:center}
.send{left:528px;top:2766px;width:124px;height:37px;background:var(--orange);color:var(--white);font-family:"Oswald",sans-serif;font-size:14px;display:flex;align-items:center;justify-content:center}
</style>
</head>
<body>

<section class="abs hero" role="img" aria-label="Photo of a wooden beer barrel with tap, a foaming mug and pint glass, wheat stalks and hops on a table"></section>
<div class="abs hero-nav-brand"><span class="dot" style="width:26px;height:26px;background:var(--amber)"></span>HALVARD</div>
<nav class="abs hero-nav">
  <span style="left:893px">About</span>
  <span style="left:965px">Menu</span>
  <span style="left:1032px">Gallery</span>
  <span style="left:1106px">Contact</span>
</nav>
<h1 class="abs hero-title">HALVARD<br>BREWERY</h1>
<div class="abs hero-mark"><span class="dot" style="width:30px;height:30px;background:var(--ink)"></span>HALVARD</div>
<span class="abs slide-num" style="top:476px">01</span>
<span class="abs slide-num" style="top:536px">02</span>
<span class="abs slide-num" style="top:596px">03</span>
<div class="abs book">BOOK A TABLE</div>

<section class="abs perfection" role="img" aria-label="Close-up of beer foam bubbles"></section>
<h2 class="abs heading" style="left:0;top:742px;width:1200px;font-size:28px">PERFECTION</h2>
<p class="abs lorem" style="left:0;top:786px;width:1200px">Lorem ipsum dolor sit amet, consectetur adipiscing elit.</p>

<div class="abs side-card" style="left:0" role="img" aria-label="Dim photo of beer glasses at a bar">
  <h3>BROWERY</h3><div class="rule"></div>
  <p class="lorem">Lorem ipsum dolor sit amet, consectetur adipiscing elit.</p>
</div>
<div class="abs center-card">
  <div class="abs center-mark"><span class="dot" style="width:180px;height:180px;background:#4a1a12"></span>HALVARD</div>
  <h3 class="abs heading" style="left:0;top:300px;width:340px;font-size:22px">SPECIALITIES</h3>
  <div class="abs" style="left:150px;top:336px;width:40px;height:1px;background:var(--amber)"></div>
  <p class="abs lorem" style="left:0;top:358px;width:340px">Lorem ipsum dolor sit amet, consectetur adipiscing elit.</p>
</div>
<div class="abs side-card" style="left:810px" role="img" aria-label="Dim photo of a pint of dark beer on a wooden table">
  <h3>BEER</h3><div class="rule"></div>
  <p class="lorem">Lorem ipsum dolor sit amet, consectetur adipiscing elit.</p>
</div>
<p class="abs" style="left:0;top:1338px;width:1200px;text-align:center;font-size:10px;font-weight:600;color:var(--amber);letter-spacing:1px">CHECK OUR DETAILS</p>

<section class="abs details-bg" role="img" aria-label="Close-up of chilled amber beer bottles with caps"></section>
<div class="abs details-box"></div>
<div class="abs details-inner"></div>
<h2 class="abs heading" style="left:368px;top:1552px;width:463px;font-size:28px;color:var(--white)">DETAILS</h2>
<p class="abs lorem" style="left:368px;top:1602px;width:463px">Lorem ipsum dolor sit amet, consectetur adipiscing elit.</p>
<p class="abs" style="left:368px;top:1663px;width:463px;text-align:center;font-size:10px;font-weight:600;color:var(--amber)">PREPARATION OF OUR DISHES</p>

<section class="abs how-bg" role="img" aria-label="Macro photo of golden beer with foam bubbles"></section>
<h2 class="abs heading" style="left:0;top:1912px;width:1200px;font-size:28px;color:var(--ink)">HOW WE REACH THIS</h2>
<p class="abs lorem" style="left:0;top:1958px;width:1200px;color:#5a3a08">Lorem ipsum dolor sit amet, consectetur adipiscing elit.</p>

<div class="abs feature" style="left:10px"><h4>DIFFRENT LOCATIONS</h4><p class="lorem">Lorem ipsum dolor sit amet, consectetur adipiscing elit.</p></div>
<div class="abs feature dark" style="left:409px"><h4>FRESH PRODUCTS</h4><p class="lorem">Lorem ipsum dolor sit amet, consectetur adipiscing elit.</p></div>
<div class="abs feature" style="left:808px"><h4>THE BEST FROM THE BEGGINING</h4><p class="lorem">Lorem ipsum dolor sit amet, consectetur adipiscing elit.</p></div>

<div class="abs footer-line"></div>
<div class="abs" style="left:520px;top:2340px;width:160px;display:flex;align-items:center;justify-content:center;gap:8px;font-weight:700;font-size:20px;color:var(--ink)"><span class="dot" style="width:18px;height:18px;background:var(--ink)"></span>HALVARD</div>
<p class="abs" style="left:0;top:2421px;width:1200px;text-align:center;font-size:11px;font-weight:700;color:var(--ink)">Ardent Taproom</p>
<p class="abs" style="left:0;top:2443px;width:1200px;text-align:center;font-size:9px;color:#8a5a08">Brewed with care in every single batch</p>
<div class="abs social" style="left:400px"></div>
<div class="abs social" style="left:450px"></div>
<div class="abs social" style="left:500px"></div>
<div class="abs social" style="left:550px"></div>
<div class="abs social" style="left:600px"></div>
<div class="abs social" style="left:650px"></div>
<div class="abs social" style="left:700px"></div>
<div class="abs social" style="left:750px"></div>

<section class="abs news"></section>
<div class="abs mug" role="img" aria-label="Photo of a tall glass beer mug with foam"></div>
<h2 class="abs news-title">Subrscribe our newsletter</h2>
<div class="abs email">WRITE YOUR E-MAIL ADRES</div>
<div class="abs send">SEND E-MAIL</div>

</body>
</html>
```